Business Executives Need Book Cover Design

We need a custom book cover instead of the boring stock cover that was available on PrintHollow.
The current cover can be seen at:
http://www.bookvarrow.example/Ledger-Lessons-Leaders-Planners-hoped/dp/7302846150
We like this cover in general (the colors, general layout and picture), but you can see it needs help with the spacing of the Authors names and general design. Also, since it is stock, someone else could have the same cover. It is for business executives so it should be classy. It should communicate that it is for executives. The book is only available in soft cover.

Target Market(s)

Business School students, business executives

Industry/Entity Type

Business

Requirements
Must have
• book name and authors names.

```html
<!DOCTYPE html>
<html lang="en">
<head>
<meta charset="utf-8">
<title>Financial Metrics for MBA's &amp; Financial Managers – Cover</title>
<link rel="stylesheet" href="https://fonts.googleapis.com/css2?family=Antonio:wght@600;700&family=Arimo:wght@400&display=swap">
<style>
  :root {
    --page-bg: #ededee;
    --cover-tan: #c99e7a;
    --title-red: #9c2f34;
    --spine-red: #8d2a2d;
    --subtitle-white: #ffffff;
    --author-ink: #2b2220;
    --photo-dark: #2a2624;
    --photo-mid: #5a524d;
    --photo-warm: #8a7560;
  }
  * { margin: 0; padding: 0; box-sizing: border-box; }
  html, body {
    width: 1200px;
    height: 1042px;
    overflow: hidden;
    background: var(--page-bg);
  }
  .cover {
    position: absolute;
    left: 297px;
    top: 41px;
    width: 606px;
    height: 960px;
    background: var(--cover-tan);
    overflow: hidden;
  }
  .cover__spine-edge {
    position: absolute;
    left: 0;
    top: 0;
    width: 16px;
    height: 100%;
    background: var(--spine-red);
  }
  .cover__title {
    position: absolute;
    left: 16px;
    right: 0;
    top: 156px;
    text-align: center;
    font-family: "Antonio", "Arial Narrow", sans-serif;
    white-space: nowrap;
  }
  .cover__title-main {
    display: block;
    color: var(--title-red);
    font-weight: 700;
    font-size: 78px;
    line-height: 1;
    letter-spacing: -0.5px;
    text-transform: uppercase;
  }
  .cover__title-sub {
    display: block;
    margin-top: 8px;
    color: var(--subtitle-white);
    font-weight: 600;
    font-size: 48px;
    line-height: 1.05;
    letter-spacing: -0.5px;
  }
  .cover__photo {
    position: absolute;
    left: 16px;
    right: 0;
    top: 375px;
    height: 454px;
    background:
      radial-gradient(ellipse 40% 55% at 22% 40%, var(--photo-warm) 0%, rgba(138,117,96,0) 70%),
      radial-gradient(ellipse 45% 60% at 85% 35%, var(--photo-mid) 0%, rgba(90,82,77,0) 75%),
      linear-gradient(160deg, #4b4541 0%, var(--photo-dark) 55%, #1c1a19 100%);
  }
  .cover__authors {
    position: absolute;
    right: 44px;
    top: 850px;
    font-family: "Arimo", Arial, sans-serif;
    font-size: 22px;
    letter-spacing: -0.3px;
    color: var(--author-ink);
    white-space: nowrap;
  }
</style>
</head>
<body>
  <main class="cover">
    <div class="cover__spine-edge"></div>
    <h1 class="cover__title">
      <span class="cover__title-main">Financial Metrics</span>
      <span class="cover__title-sub">for MBA's &amp; Financial Managers</span>
    </h1>
    <div class="cover__photo" role="img" aria-label="Photograph of a stack of gold coins beside a businessman in a suit touching a glowing rising bar chart with a red trend arrow"></div>
    <p class="cover__authors">Daniel Hartwell &amp; Robert K. Linsome</p>
  </main>
</body>
</html>
```